Crestline Athletics and fitness is Hosting a Winter Renewal yoga class. World-renowned Rob Calloway will be teaching. Rob is a Life Empowerment Coach. This event will take place on January 5th, 2019 Time: 2pm - 4pmYoga at Optimum Sports and FitnessCost: $30 / $40 at the Door

Requirements
Must have
• Crestline Athletics and fitness Logo
• Crestline Lotus Yoga Logo

```html
<!DOCTYPE html>
<html lang="en">
<head>
<meta charset="utf-8">
<title>Winter Renewal Yoga Class – Crestline Athletics and Fitness</title>
<link rel="stylesheet" href="https://fonts.googleapis.com/css2?family=Lilita+One&family=Source+Sans+3:wght@700&family=Mulish:wght@300&display=swap">
<style>
  :root {
    --bg: #e9e6e2;
    --red: #f01a24;
    --black: #000000;
    --white: #ffffff;
    --sun-edge: #f3f3f3;
  }
  * { box-sizing: border-box; margin: 0; padding: 0; }
  html, body { width: 1200px; height: 1200px; overflow: hidden; background: var(--bg); }
  .flyer {
    position: absolute; left: 201px; top: 40px;
    width: 797px; height: 1120px;
    background: var(--red); overflow: hidden;
    font-family: "Source Sans 3", sans-serif; font-weight: 700; color: var(--white);
  }
  .brand-tab {
    position: absolute; left: 152px; top: 0; width: 479px; height: 167px;
    background: var(--white); border-radius: 0 0 44px 44px;
    display: flex; align-items: center; justify-content: center; gap: 18px;
  }
  .brand-dot { width: 100px; height: 100px; border-radius: 50%; background: var(--red); flex: none; }
  .brand-name {
    color: var(--red); font-family: "Source Sans 3", sans-serif; font-weight: 700;
    font-size: 30px; line-height: 1.05; text-transform: uppercase; letter-spacing: 1px;
  }
  .headline {
    position: absolute; left: 0; right: 0; top: 190px; text-align: center;
    font-family: "Lilita One", sans-serif; font-weight: 400; font-size: 47px;
    letter-spacing: 1px; text-transform: uppercase;
  }
  .hero-art { position: absolute; left: 150px; top: 288px; width: 418px; height: 418px; }
  .ground { position: absolute; left: 0; right: 0; top: 700px; bottom: 0; background: var(--black); }
  .line { position: absolute; left: 0; right: 0; text-align: center; white-space: nowrap; }
  .teacher { top: 770px; font-size: 31px; }
  .when { top: 840px; font-size: 35px; }
  .when .sep { display: inline-block; margin: 0 28px; }
  .venue { top: 893px; font-size: 31px; }
  .cost {
    position: absolute; left: 121px; top: 972px; width: 549px; height: 71px;
    border: 2px solid var(--white);
    display: flex; align-items: center; justify-content: center; font-size: 35px;
  }
  .cost .price { color: var(--red); margin: 0 8px; }
  .site { top: 1066px; font-family: "Mulish", sans-serif; font-weight: 300; font-size: 25px; }
</style>
</head>
<body>
  <main class="flyer">
    <header class="brand-tab">
      <span class="brand-dot"></span>
      <span class="brand-name">Crestline Athletics<br>and Fitness</span>
    </header>

    <h1 class="headline">Winter Renewal Yoga Class</h1>

    <svg class="hero-art" viewBox="0 0 418 418" role="img" aria-label="Silhouette of a yoga instructor in warrior pose in front of a large setting sun">
      <defs>
        <radialGradient id="sun-glow" cx="50%" cy="50%" r="50%">
          <stop offset="0%" stop-color="#ffffff"/>
          <stop offset="100%" stop-color="#f3f3f3"/>
        </radialGradient>
      </defs>
      <circle cx="209" cy="209" r="209" fill="url(#sun-glow)"/>
    </svg>

    <section class="ground">
    </section>

    <p class="line teacher">Teach by World-renowned ROB CALLOWAY</p>
    <p class="line when">January 5th, 2019<span class="sep">|</span>2pm - 4pm</p>
    <p class="line venue">@ CRESTLINE ATHLETICS AND FITNESS</p>
    <div class="cost">Cost:<span class="price">$30 / $40</span>at the Door</div>
    <p class="line site">www.crestlineaf.com</p>
  </main>
</body>
</html>
```